DELCOUR ROOFING YARD SIGN

We need a yard sign to put in our customers' yards when we are roofing their home.
Delcour Roofing
438 Fenwick Rd
Lake Charles LA 70615
phone: 337-555-0142

Maybe some verbiage like "Your Hometown Roofing Experts"
or
"Family Owned Since 1956"

```html
<!DOCTYPE html>
<html lang="en">
<head>
<meta charset="utf-8">
<title>Delcour Roofing Yard Sign</title>
<link href="https://fonts.googleapis.com/css2?family=Lora:wght@500;600;700&display=swap" rel="stylesheet">
<style>
  :root {
    --brand-blue: #283891;
    --ink: #231f20;
    --paper: #ffffff;
    --canvas: #ffffff;
  }
  * { margin: 0; padding: 0; box-sizing: border-box; }
  html, body {
    width: 1200px;
    height: 960px;
    overflow: hidden;
    background: var(--canvas);
  }
  .yard-sign {
    position: absolute;
    left: 52px;
    top: 68px;
    width: 1055px;
    height: 792px;
    transform: scale(1.04);
    transform-origin: top left;
    background: var(--paper);
    border: 1px solid var(--ink);
    overflow: hidden;
    font-family: "Lora", Georgia, serif;
  }
  .sign-shapes {
    position: absolute;
    inset: 0;
  }
  .badge-name {
    position: absolute;
    left: 378px;
    top: 172px;
    width: 300px;
    text-align: center;
    color: var(--ink);
    font-weight: 700;
    font-size: 40px;
    line-height: 1.15;
    letter-spacing: 0.5px;
  }
  .contact-rule {
    position: absolute;
    left: 55px;
    width: 948px;
    height: 3px;
    background: var(--ink);
  }
  .contact-rule.top { top: 436px; }
  .contact-rule.bottom { top: 601px; }
  .pin-icon {
    position: absolute;
    left: 83px;
    top: 471px;
    width: 60px;
    height: 90px;
  }
  .address {
    position: absolute;
    left: 177px;
    top: 465px;
    color: var(--ink);
    font-size: 33px;
    font-weight: 600;
    line-height: 32px;
  }
  .phone-icon {
    position: absolute;
    left: 463px;
    top: 473px;
    width: 78px;
    height: 78px;
  }
  .phone-number {
    position: absolute;
    left: 561px;
    top: 470px;
    color: var(--ink);
    font-size: 73px;
    font-weight: 700;
    line-height: 88px;
    letter-spacing: 0.5px;
  }
  .tagline-band {
    position: absolute;
    left: 0;
    top: 654px;
    width: 100%;
    height: 138px;
    background: var(--brand-blue);
    color: var(--paper);
    font-size: 45px;
    font-weight: 700;
    text-align: center;
    line-height: 138px;
    padding-right: 16px;
    letter-spacing: 0.3px;
  }
</style>
</head>
<body>
  <div class="yard-sign">
    <svg class="sign-shapes" width="1055" height="792" viewBox="0 0 1055 792">
      <polygon points="0,0 1055,0 1055,158 695,237 362,237 0,160" fill="var(--brand-blue)"/>
      <circle cx="528" cy="222" r="168" fill="var(--paper)"/>
      <circle cx="528" cy="222" r="156" fill="none" stroke="var(--ink)" stroke-width="4"/>
    </svg>

    <div class="badge-name">Delcour<br>Roofing</div>

    <div class="contact-rule top"></div>

    <svg class="pin-icon" viewBox="0 0 60 90" aria-hidden="true">
      <path d="M30 0C13.4 0 0 13.4 0 30c0 16 30 60 30 60s30-44 30-60C60 13.4 46.6 0 30 0z" fill="var(--brand-blue)"/>
      <circle cx="30" cy="29" r="11" fill="var(--paper)"/>
    </svg>

    <div class="address">
      <div class="address-name">Delcour Roofing</div>
      <div class="address-street">438 Fenwick Rd</div>
      <div class="address-zip">LA 70615</div>
    </div>

    <svg class="phone-icon" viewBox="0 0 78 78" aria-hidden="true">
      <circle cx="39" cy="39" r="39" fill="var(--brand-blue)"/>
      <path d="M26 17c2-1 4 0 5 2l5 9c1 2 0 4-1 5l-3 3c2 5 6 10 11 13l3-3c1-1 3-2 5-1l9 5c2 1 3 3 2 5l-3 6c-2 3-6 4-9 3-15-5-27-17-32-32-1-3 0-7 3-9z" fill="var(--paper)"/>
    </svg>

    <div class="phone-number">337-555-0142</div>

    <div class="contact-rule bottom"></div>

    <div class="tagline-band">Your Hometown Roofing Experts</div>
  </div>
</body>
</html>
```